Book cover design for a book named BLOOM

Hello Designers,
The name of the book is BLOOM and it is about unexpected experiences individuals have which are beyond their control. Occurrences they are unable to overcome or get out of themselves without the help of God. After overcoming these situations they know only God could have done this for them, no one else could have. It is an adult Christian book. I would like you to be as creative as you can with the cover, using color, light, graphic designs, shapes, scale, lines etc. (you are the designers, I don't know how to do these things.) I would like to use the image created on a paperback, hardcover or e book. I tried to use an image from Pixmarble just to give you some idea of my thinking but you do not have to use these hands. The hands should look as if they are giving someone the word TESTIMONY not receiving it. Use of the words provided, the light rays, and some type of hands extended should not change, but how you use them is up to you. Use the words, light rays, and hands however you wish as long as they convey someone giving the word TESTIMONY. The word TESTIMONY should be proportional to the hand in size and should appear as if being held in the actual hand it should not be larger than the book name. It is a Christian book of testimonies. Also for your design samples you can use the name Marlene Quiller for the author. Thank you, please feel free to contact me if you have any questions. I am looking for the cover to be an attention grabber and give the reader something to really think about and remember visually when they see this cover. Thank you again.

Target Market(s)

anyone and christians

Requirements
Must have
• Use of the words provided, the light rays, and some type of hands extended should not change.
Nice to have
• be as creative as you can with the cover, using color, light, graphic designs, shapes, scale, lines etc. (you are the designers, I don't know how to do these things.)
Should not have
• It should not have fonts, colors, etc. that convey it is a child's book, fairytale, or fictional etc. It is a book of true stories that actually happened. It should not look exactly like my example, what I provided.

```html
<!DOCTYPE html>
<html lang="en">
<head>
<meta charset="utf-8">
<title>BLOOM – Book Cover</title>
<link rel="stylesheet" href="https://fonts.googleapis.com/css2?family=Alfa+Slab+One&family=Cabin:wght@600&family=Oswald:wght@400&family=Roboto:wght@700&display=swap">
<style>
  :root {
    --ink-night: #000000;
    --ray-blue: #5a73b8;
    --ray-glow: #c9d4f2;
    --hand-skin: #d9cfe0;
    --hand-shadow: #8d7f96;
    --title-white: #ffffff;
    --promise-red: #d7191f;
    --testimony-black: #0a0a0a;
  }
  html, body {
    margin: 0;
    padding: 0;
    width: 799px;
    height: 1200px;
    overflow: hidden;
    background: var(--ink-night);
  }
  .cover {
    position: relative;
    width: 799px;
    height: 1200px;
    overflow: hidden;
    background: var(--ink-night);
  }
  .light-rays {
    position: absolute;
    inset: 0;
    background:
      radial-gradient(ellipse 120px 520px at 400px 700px, rgba(201,212,242,0.75), rgba(90,115,184,0.35) 55%, transparent 100%),
      radial-gradient(ellipse 330px 720px at 400px 430px, rgba(90,115,184,0.55), rgba(40,55,100,0.25) 60%, transparent 100%),
      linear-gradient(180deg, #0b1020 0%, #000 45%, #000 100%);
  }
  .offering-hands {
    position: absolute;
    left: 0;
    top: 765px;
    width: 799px;
    height: 435px;
    background:
      radial-gradient(ellipse 170px 160px at 400px 120px, #ffffff, rgba(255,255,255,0) 100%),
      radial-gradient(ellipse 360px 200px at 400px 170px, var(--hand-skin) 0%, #b7aac0 65%, rgba(60,50,60,0.6) 90%, transparent 100%),
      linear-gradient(180deg, transparent 0%, #000 100%);
  }
  .title-block {
    position: absolute;
    left: 0;
    top: 80px;
    width: 799px;
  }
  .book-title {
    display: block;
  }
  .book-title text {
    font-family: "Alfa Slab One", serif;
    fill: var(--title-white);
  }
  .tagline {
    margin: 22px 0 0;
    font-family: "Cabin", sans-serif;
    font-weight: 600;
    font-size: 34px;
    line-height: 44px;
    letter-spacing: -0.6px;
    color: var(--title-white);
    text-align: center;
  }
  .held-word {
    position: absolute;
    left: 0;
    top: 840px;
    width: 799px;
  }
  .promise {
    margin: 0;
    font-family: "Roboto", sans-serif;
    font-weight: 700;
    font-size: 28px;
    letter-spacing: 0.6px;
    color: var(--promise-red);
    text-align: center;
  }
  .testimony {
    display: block;
    margin-top: -2px;
  }
  .testimony text {
    font-family: "Oswald", sans-serif;
    font-weight: 400;
    fill: var(--testimony-black);
  }
</style>
</head>
<body>
  <main class="cover">
    <div class="light-rays" role="img" aria-label="Beams of blue-white light streaming downward from above"></div>
    <div class="offering-hands" role="img" aria-label="Two open cupped hands extended forward, glowing with light"></div>

    <header class="title-block">
      <svg class="book-title" width="799" height="140" viewBox="0 0 799 140">
        <text x="71" y="132" textLength="651" lengthAdjust="spacingAndGlyphs" font-size="172">BLOOM</text>
      </svg>
      <p class="tagline">Before there will ever be a TESTIMONY<br>there must always be an experience.</p>
    </header>

    <section class="held-word">
      <p class="promise">OUT OF THE TEST I'VE GIVEN YOU A</p>
      <svg class="testimony" width="799" height="120" viewBox="0 0 799 120">
        <text x="139" y="114" textLength="517" lengthAdjust="spacingAndGlyphs" font-size="150">TESTIMONY</text>
      </svg>
    </section>
  </main>
</body>
</html>
```